Beauty Salon Treatment Menu & Pricing

We need a Treatment Pricelist/ Brochure made to hand out to potential & existing customers! Meadowlark Body & Makeup is a small friendly beauty salon focused on the beauty essentials such as waxing, spray tanning, facials & makeup. We have a webpage with our colour theme and style and we would like to brochure to tie in.
www.meadowlarkbodyandmakeup.example.au.
We like a brochure that is clean, simple and easy to read.

Industry/Entity Type

Beauty Salon

```html
<!DOCTYPE html>
<html lang="en">
<head>
<meta charset="utf-8">
<title>Meadowlark Body &amp; Makeup – Price List</title>
<link href="https://fonts.googleapis.com/css2?family=Open+Sans:wght@400;600;700&family=Arimo:ital,wght@0,400;0,700;1,400&family=Crimson+Text:ital@1&display=swap" rel="stylesheet">
<style>
:root{
  --coral:#e5483f;
  --ink:#231f20;
  --white:#ffffff;
  --stage:#bdbdbd;
  --rule:#e5483f;
}
*{box-sizing:border-box;margin:0;padding:0}
html,body{width:855px;height:1200px;overflow:hidden;background:var(--stage)}
body{position:relative;font-family:'Arimo',Arial,sans-serif;color:var(--ink)}

.cover{position:absolute;left:17px;top:14px;width:821px;height:581px;background:var(--coral);color:var(--white);border:1px solid #444}
.cover-col{position:absolute;top:48px;width:157px}
.cover-col.left{left:34px}
.cover-col.right{left:221px}
.cover h2{font-family:'Open Sans',sans-serif;font-weight:700;font-size:10.5px;letter-spacing:.2px;margin-bottom:11px}
.cover .section+ .section{margin-top:16px}
.row{display:flex;align-items:baseline;font-size:6.6px;font-weight:700;height:14.7px;line-height:14.7px}
.row .dots{flex:1;border-bottom:1px dotted currentColor;margin:0 2px;transform:translateY(-2px)}
.row em{font-weight:400}
.note{font-size:6.4px;font-style:italic;height:14.7px;line-height:14.7px}
.gap{height:14.7px}

.photo{position:absolute;right:0;top:0;width:411px;height:478px;background:radial-gradient(ellipse at 65% 55%,#d9d9d9 0%,#9a9a9a 45%,#3a3a3a 100%)}
.contact{position:absolute;left:40px;top:500px;width:340px;text-align:center;font-size:7.6px;font-weight:700;line-height:13.7px}
.brand{position:absolute;left:521px;top:500px;width:190px;text-align:center;font-family:'Open Sans',sans-serif;font-weight:400;color:var(--white)}
.brand .name{font-size:29px;letter-spacing:3px;line-height:34px}
.brand .tag{font-size:12.5px;letter-spacing:3px;line-height:18px}

.menu{position:absolute;left:17px;top:606px;width:823px;height:582px;background:var(--white);border:1px solid #444}
.menu h1{position:absolute;left:37px;top:36px;font-family:'Open Sans',sans-serif;font-weight:600;font-size:18px;color:var(--coral);letter-spacing:.3px}
.menu .top-rule{position:absolute;left:37px;top:64px;width:751px;height:2px;background:var(--rule)}
.menu .foot-rule{position:absolute;left:50px;top:553px;width:738px;height:1px;background:#f0a49f}
.menu .foot-mark{position:absolute;left:37px;top:545px;width:9px;height:9px;border:1.5px solid var(--coral)}
.col{position:absolute;top:86px}
.col.c1{left:36px;width:182px}
.col.c2{left:235px;width:166px}
.col.c3{left:423px;width:177px}
.col.c4{left:616px;width:172px}
.menu h3{font-family:'Open Sans',sans-serif;font-weight:600;font-size:10.5px;color:var(--coral);margin-top:-2px;margin-bottom:12px}
.treat{margin-bottom:16px}
.treat .row{color:var(--coral);font-weight:700;font-size:6.9px}
.treat .row .dots{border-color:var(--ink)}
.treat .price{color:var(--ink)}
.time{font-size:6.4px;font-style:italic;font-weight:700;line-height:14.7px}
.treat p{font-size:6.9px;line-height:14.7px;text-align:justify}
.treat p.aside{font-style:italic;font-size:6.4px}
.c4 .row{font-size:6.6px}
.c4 .intro{font-size:6.4px;font-style:italic;line-height:14.7px;text-align:justify}
.c4 .block{margin-bottom:16px}
.quote{font-family:'Crimson Text',serif;font-style:italic;font-size:9.6px;line-height:12.6px;text-align:center;color:#4a4a4a;padding:0 8px}
.hours{position:absolute;left:616px;top:451px;width:172px;height:92px;background:var(--coral);color:var(--white);text-align:center;padding-top:9px}
.hours h4{font-family:'Open Sans',sans-serif;font-weight:600;font-size:9.5px;margin-bottom:6px}
.hours p{font-size:7.4px;font-weight:700;line-height:14.7px}
</style>
</head>
<body>

<section class="cover">
  <div class="cover-col left">
    <div class="section">
      <h2>FACIAL WAXING/ TINT</h2>
      <div class="row"><span>Eyebrow</span><span class="dots"></span><span>$18.00</span></div>
      <div class="row"><span>Brow wax &amp; tint</span><span class="dots"></span><span>$30.00</span></div>
      <div class="row"><span>Lip or chin or sides</span><span class="dots"></span><span>$10.00</span></div>
      <div class="row"><span>Brow, lip &amp; chin</span><span class="dots"></span><span>$33.00</span></div>
      <div class="row"><span>Full face</span><span class="dots"></span><span>$38.00</span></div>
      <div class="row"><span>Lash tint</span><span class="dots"></span><span>$20.00</span></div>
      <div class="row"><span>Brow tint</span><span class="dots"></span><span>$16.00</span></div>
      <div class="row"><span>Lash &amp; brow tint</span><span class="dots"></span><span>$30.00</span></div>
    </div>
    <div class="section">
      <h2>FEMALE WAXING</h2>
      <div class="row"><span>Brazilian</span><span class="dots"></span><span>$45.00</span></div>
      <div class="row"><span>Extended bikini</span><span class="dots"></span><span>$30.00</span></div>
      <div class="row"><span>Bikini</span><span class="dots"></span><span>$18.00</span></div>
      <div class="row"><span>Full leg</span><span class="dots"></span><span>$45.00</span></div>
      <div class="row"><span>Full leg &amp; bikini</span><span class="dots"></span><span>$58.00</span></div>
      <div class="row"><span>Full leg &amp; brazilian</span><span class="dots"></span><span>$85.00</span></div>
      <div class="row"><span>Half leg <em><i>(inc knees)</i></em></span><span class="dots"></span><span>$30.00</span></div>
      <div class="row"><span>Half leg &amp; bikini</span><span class="dots"></span><span>$43.00</span></div>
      <div class="row"><span>Half leg &amp; brazilian</span><span class="dots"></span><span>$70.00</span></div>
      <div class="row"><span>Full arm</span><span class="dots"></span><span>$30.00</span></div>
      <div class="row"><span>Half arm</span><span class="dots"></span><span>$25.00</span></div>
      <div class="row"><span>Underarm</span><span class="dots"></span><span>$18.00</span></div>
      <div class="row"><span>Stomach</span><span class="dots"></span><span>$15.00</span></div>
      <div class="row"><span>Back</span><span class="dots"></span><span>$20.00</span></div>
      <div class="row"><span>Patches, from</span><span class="dots"></span><span>$10.00</span></div>
    </div>
  </div>

  <div class="cover-col right">
    <div class="section">
      <h2>MENS WAXING</h2>
      <div class="row"><span>Neck</span><span class="dots"></span><span>$25.00</span></div>
      <div class="row"><span>Back <em><i>(includes neck)</i></em></span><span class="dots"></span><span>$40.00</span></div>
      <div class="row"><span>Chest</span><span class="dots"></span><span>$35.00</span></div>
      <div class="row"><span>Chest &amp; stomach</span><span class="dots"></span><span>$40.00</span></div>
      <div class="row"><span>Back, chest &amp; stomach</span><span class="dots"></span><span>$75.00</span></div>
      <div class="row"><span>Full leg</span><span class="dots"></span><span>$55.00</span></div>
      <div class="row"><span>Full arm</span><span class="dots"></span><span>$38.00</span></div>
      <div class="row"><span>Underarm</span><span class="dots"></span><span>$20.00</span></div>
    </div>
    <div class="section">
      <h2>MAKEUP</h2>
      <div class="row"><span>Bridal</span><span class="dots"></span><span>$95.00</span></div>
      <div class="note">We come to you, min. 3 faces Includes lashes.</div>
      <div class="row"><span>Bridal Trial</span><span class="dots"></span><span>$100.00</span></div>
      <div class="note">Includes take home lip colour.</div>
      <div class="row"><span>Special Occasion</span><span class="dots"></span><span>$70.00</span></div>
      <div class="row"><span>School Ball</span><span class="dots"></span><span>$65.00</span></div>
      <div class="row"><span>False Lash Application</span><span class="dots"></span><span>$25.00</span></div>
      <div class="note">Includes lashes.</div>
      <div class="gap"></div>
      <div class="row"><span>Makeup Lesson 1 hour</span><span class="dots"></span><span>$100.00</span></div>
      <div class="note">Includes $60 free products.</div>
    </div>
    <div class="section">
      <h2>TANNING</h2>
      <div class="row"><span>Spray Tan <em><i>(every 10th tan free)</i></em></span><span class="dots"></span><span>$35.00</span></div>
      <div class="row"><span>Half Body Spray Tan</span><span class="dots"></span><span>$25.00</span></div>
    </div>
  </div>

  <div class="photo" role="img" aria-label="Black and white photo of a makeup artist applying eyeliner to a client"></div>

  <address class="contact" style="font-style:normal">
    42 Harbour Lane, Fernvale, WA 6999 (inside Parkside Hair Studio)<br>
    P: 0400 000 123 &nbsp;E: info@meadowlarkbodyandmakeup.example.au<br>
    www.meadowlarkbodyandmakeup.example.au<br>
    facebook.com/meadowlarkbodyandmakeup
  </address>

  <div class="brand">
    <div class="name">MEADOWLARK</div>
    <div class="tag">BODY &amp; MAKEUP</div>
  </div>
</section>

<section class="menu">
  <h1>PRICE LIST</h1>
  <div class="top-rule"></div>

  <div class="col c1">
    <h3>VERDE CLINICA FACIALS</h3>
    <div class="treat">
      <div class="row"><span>Quick Fix My Skin</span><span class="dots"></span><span class="price">$65.00</span></div>
      <div class="time">Allow 30 minutes</div>
      <p>An express facial customised to suit your current skin condition. Includes exfoliation, active serums and a powerful face mask using a combination of advanced Verde Clinica products.</p>
    </div>
    <div class="treat">
      <div class="row"><span>Glycolic Peel Treatment</span><span class="dots"></span><span class="price">$60.00</span></div>
      <div class="time">Allow 20 minutes</div>
      <p class="aside">Buy 4 and get the 6th treatment free. 1 treatment per week</p>
      <p>An active treatment combining the powerful effects of Glycolic Acid and Vitamin C to refine the skins appearance and texture, balance irregularities in skin tone and pigmentation, counteract the effect of acne, including scarring and reduce blackheads and other blemishes.</p>
    </div>
    <div class="treat">
      <div class="row"><span>Glycolic Microdermabrasion Treatment</span><span class="dots"></span><span class="price">$100.00</span></div>
      <div class="time">Allow 45 minutes</div>
      <p>This is a highly active treatment to target the skins imperfections and overall complexion. We incorporate the use of the microdermabrasion scrub and the skin refining mask to enhance the effects of the glycolic peel treatment as well as lengthen the treatment to be more relaxing and effective.</p>
    </div>
  </div>

  <div class="col c2">
    <div class="treat" style="margin-top:22px">
      <div class="row"><span>Clear Skin Facial</span><span class="dots"></span><span class="price">$80.00</span></div>
      <div class="time">Allow 45 minutes</div>
      <p>A deep cleansing facial designed to help manage and treat oily, acne and pustular skin. The treatment uses a combination of ingredients including Vitamin A, Tea Tree, multi-fruit acids, minerals and deep cleansing clays.</p>
    </div>
    <div class="treat">
      <div class="row"><span>Rebalancing Vitamin A Facial</span><span class="dots"></span><span class="price">$90.00</span></div>
      <div class="time">Allow 60 minutes</div>
      <p>A relaxing treatment for combination skin types, to detox, purify and heal the skin. The treatment incorporates the use of Vitamin A, Zinc Oxide, Stem cells, Lotus Flower liposomes, Green Tea and Ginkgo Biloba.</p>
    </div>
    <div class="treat">
      <div class="row"><span>Marine Radiance Facial</span><span class="dots"></span><span class="price">$100.00</span></div>
      <div class="time">Allow 60 minutes</div>
      <p>This gentle and rehydrating treatment is suitable for most skin types, to restore softness and radiance to the skins complexion. Oxygenating and strengthening, incorporating marine extracts, collagen and elastin. A perfect facial for the Bride-to-be!</p>
      <p class="aside">Add a Glycolic peel to enhance the benefits</p>
    </div>
  </div>

  <div class="col c3">
    <div class="treat" style="margin-top:22px">
      <div class="row"><span>Anti Stress, Sensitive Skin Treatment</span><span class="dots"></span><span class="price">$100.00</span></div>
      <div class="time">Allow 60 minutes</div>
      <p>Perfect for skin that is prone to redness, irritation, flakiness and inflammation. This treatment is super relaxing using Boswellic Acid <i>(a plant derived natural anti-inflammatory)</i> along with cehami to soothe the skin. Great for anyone who suffers from eczema, dermatitis and psoriasis. Skin will look and feel calmer.</p>
    </div>
    <div class="treat">
      <div class="row"><span>Anti Ageing Hydra Restore Facial</span><span class="dots"></span><span class="price">$120.00</span></div>
      <div class="time">Allow 60 minutes</div>
      <p>A beautiful hot oil infusion treatment that uses 100% natural vitamins and oils. Great for any sign of dehydration, dryness and wrinkles. The skin will look younger, healthier, radiant and feel amazing! Perfect for anyone who has completed a course of the glycolic peel treatments.</p>
    </div>
    <div class="treat">
      <div class="row"><span>Firming Lift Facial</span><span class="dots"></span><span class="price">$150.00</span></div>
      <div class="time">Allow 60 minutes</div>
      <p>The most luxurious and restorative facial treatment to firm, strengthen and oxygenate the skin. Using a high quality marine derived collagen, elastin and pearl extract, this facial treatment is ideal for anyone losing skin firmness and elasticity. Suitable for ages 35+. Includes caviar &amp; pearl eye treatment.</p>
    </div>
  </div>

  <div class="col c4">
    <div class="block">
      <h3>FACIAL ADD ONS</h3>
      <p class="intro">Incorporate any of the following into your facial treatment for a small cost.</p>
      <div class="row"><span>Glycolic Peel</span><span class="dots"></span><span>$20.00</span></div>
      <div class="row"><span>Firming Lift Caviar &amp;</span></div>
      <div class="row"><span>Pearl Eye Treatment</span><span class="dots"></span><span>$20.00</span></div>
      <div class="row"><span>Firming Lift Neck &amp; Bust Treatment</span><span class="dots"></span><span>$20.00</span></div>
    </div>
    <div class="block">
      <h3>NAILS</h3>
      <div class="row"><span>Luxury Manicure</span><span class="dots"></span><span>$45.00</span></div>
      <div class="row"><span>Nail file &amp; paint</span><span class="dots"></span><span>$25.00</span></div>
      <div class="row"><span>+ Gel Colour Gloss</span><span class="dots"></span><span>$10.00</span></div>
      <div class="row"><span>Gel polish removal</span><span class="dots"></span><span>$15.00</span></div>
      <div class="gap" style="height:7px"></div>
      <div class="row"><span>Luxury Pedicure</span><span class="dots"></span><span>$55.00</span></div>
      <div class="row"><span>Toe nail file &amp; paint</span><span class="dots"></span><span>$35.00</span></div>
      <div class="row"><span>+ Gel Colour Gloss</span><span class="dots"></span><span>$10.00</span></div>
      <div class="row"><span>Gel polish removal</span><span class="dots"></span><span>$15.00</span></div>
    </div>
    <p class="quote">Here at Meadowlark Body &amp; Makeup we strive to make sure you leave your appointment with expectations exceeded. We tailor our services to the individual, ensuring our clients leave happy and satisfied!</p>
  </div>

  <div class="hours">
    <h4>OPENING HOURS</h4>
    <p>Tue-Wed: 9.00 am - 5:00 pm</p>
    <p>Thu: 11.00 am - 8.00 pm</p>
    <p>Fri: 9.00 am - 5:00 pm</p>
    <p>Sat: 8.00 am - 2.00 pm</p>
  </div>

  <div class="foot-mark"></div>
  <div class="foot-rule"></div>
</section>

</body>
</html>
```